A start-up named "brivora" - a clinical research organization needs a new PowerPoint design

We need a new PowerPoint Design (incl. business card and stationery design) for an early-stage start-up named "brivora" seeking to build an ecosystem/ strategic partner alliances or consortium of committed and active collaborators to guide important components of the clinical trial.

Our ultimate goal is to avoid false neutrals – therapies that have not been and may never be evaluated in clinical trials due to the costs and/ or complexity.

The final design should highlight our patient-centric approach, innovative study design supported with the novel AI platform to make a stronger impact on patient lives.

Please see the attached brief for more details.
Updates

Requesting the proposals on color-coding, business-card designs, clinical research visuals, and icons as well as stationery design.

Target Market(s)

Pharma/ Biotech Executives
Medical Institutions
Clinical Trial Participants (Patients)

Colors
e34398

Requirements
Must have
• Use the Color Version of purple/ magenta logo

```html
<!DOCTYPE html>
<html lang="en">
<head>
<meta charset="utf-8">
<title>brivora – Presentation Template</title>
<link href="https://fonts.googleapis.com/css2?family=Nunito:wght@400;600;700;800&display=swap" rel="stylesheet">
<style>
  :root{
    --canvas:#1b1b1b;
    --white:#ffffff;
    --ink:#1c1f2e;
    --body:#3a3a3a;
    --magenta:#c8267f;
    --brand:#4a35c4;
    --blue:#1f63c9;
    --purple:#7a1fc0;
    --badge:#2e8a0c;
    --orange:#e2461b;
    --berry:#c0135f;
    --grey:#bdbdbd;
  }
  *{box-sizing:border-box;margin:0;padding:0}
  html,body{width:1200px;height:3943px;overflow:hidden;background:var(--canvas)}
  body{font-family:"Nunito",sans-serif;color:var(--body);position:relative}
  .slide{position:absolute;left:52px;width:1096px;height:617px;background:var(--white);overflow:hidden}
  .badge{position:absolute;right:-2px;top:-2px;width:58px;height:58px;border-radius:50%;background:var(--badge);border:3px solid var(--white);color:var(--white);font-size:15px;font-weight:700;display:flex;align-items:center;justify-content:center;padding:0 0 2px 0}
  .page-code{position:absolute;right:10px;bottom:6px;font-size:12px;color:#555}
  .abs{position:absolute}
  .wordmark{font-weight:800;color:var(--brand);letter-spacing:-1px;display:flex;align-items:center;gap:10px;line-height:1}
  .wordmark .dot{width:16px;height:16px;background:var(--brand)}
  .rule{position:absolute;height:5px;width:137px;background:linear-gradient(90deg,var(--blue),var(--purple))}
  .heading{font-weight:600;color:var(--magenta);line-height:1}
  .copy{font-size:12.3px;line-height:25.6px;color:var(--body)}
  .copy p+p{margin-top:25px}
  .bullets{list-style:none}
  .bullets li{font-size:16px;line-height:37.6px;color:var(--body);display:flex;align-items:center;gap:12px}
  .bullets svg{flex:none}
</style>
</head>
<body>

<!-- Slide 1: Welcome -->
<section class="slide" style="top:57px">
  <div class="wordmark abs" style="left:17px;top:66px;font-size:74px">brivora<span class="dot"></span></div>
  <h1 class="abs" style="left:17px;top:226px;font-size:58px;font-weight:600;color:var(--ink)">Welcome</h1>
  <div class="rule" style="left:17px;top:311px"></div>
  <div class="copy abs" style="left:17px;top:336px;width:362px">Maecenas vel tortor accumsan quam varius imperdiet vel eget elit. Aenean facilisis tincidunt lectus, id dictum nisi luctus eget. Vivamus efficitur ex condimentum, malesuada eros eget, feugiat nibh. Sed tellus ex, imperdiet eget gravida sit amet, volutpat eget turpis. In nec ultricies est. Etiam mattis augue vehicula odio posuere.</div>
  <svg class="abs" style="left:392px;top:0" width="704" height="617" role="img" aria-label="Molecular network illustration in magenta and violet">
    <defs>
      <radialGradient id="net" cx="0.7" cy="0.4" r="0.8">
        <stop offset="0" stop-color="#7b4fc9" stop-opacity="0.35"/>
        <stop offset="0.6" stop-color="#c23a8a" stop-opacity="0.18"/>
        <stop offset="1" stop-color="#ffffff" stop-opacity="0"/>
      </radialGradient>
    </defs>
    <rect width="704" height="617" fill="url(#net)"/>
  </svg>
  <div class="badge">1</div>
  <div class="page-code">M2</div>
</section>

<!-- Slide 2: Text with lab image -->
<section class="slide" style="top:698px">
  <svg class="abs" style="left:0;top:0" width="600" height="617" role="img" aria-label="Photo of scientists working at a microscope in a laboratory">
    <defs>
      <linearGradient id="lab1" x1="0" y1="0" x2="1" y2="1">
        <stop offset="0" stop-color="#d9dde2"/>
        <stop offset="0.5" stop-color="#b7bcc3"/>
        <stop offset="1" stop-color="#eceef0"/>
      </linearGradient>
    </defs>
    <polygon points="108,0 591,0 527,617 0,617" fill="url(#lab1)"/>
  </svg>
  <h2 class="heading abs" style="left:626px;top:56px;font-size:40px">Proin eget congue nulla</h2>
  <div class="rule" style="left:626px;top:119px"></div>
  <div class="copy abs" style="left:626px;top:145px;width:455px">
    <p>Fusce sollicitudin lorem et luctus volutpat. Proin placerat dapibus gravida. In tristique tristique nulla eget hendrerit. Maecenas vel tortor accumsan quam varius imperdiet vel eget elit. Aenean facilisis tincidunt lectus, id dictum nisi luctus eget. Vivamus efficitur ex condimentum, malesuada eros eget, feugiat nibh. Sed tellus ex, imperdiet eget gravida sit amet, volutpat eget turpis. In nec ultricies est. Etiam mattis augue vehicula odio posuere, sit amet tempus lectus luctus. Nulla facilisi. Etiam vel massa elementum, bibendum tellus venenatis, feugiat massa. Curabitur venenatis lacinia ornare. Cras sollicitudin cursus dui eu placerat.</p>
    <p>Quisque aliquet ex nec est vestibulum pulvinar. Pellentesque convallis molestie enim sit amet efficitur. Etiam id imperdiet lectus. Vivamus lacus justo, ultrices nec erat in, euismod iaculis mauris. Vivamus eleifend vitae nulla vel malesuada. In ac malesuada lacus, et consectetur ante. Fusce vitae lectus sit amet mi pulvinar maximus. Aenean placerat, nibh vel accumsan aliquet, magna nibh accumsan nibh, ac tempus nunc ipsum ac tellus.</p>
  </div>
  <div class="badge">2</div>
  <div class="page-code">M2</div>
</section>

<!-- Slide 3: Statement with wide image -->
<section class="slide" style="top:1341px">
  <svg class="abs" style="left:0;top:0" width="1096" height="450" role="img" aria-label="Photo of gloved hands scanning blood sample tubes in a rack">
    <defs>
      <linearGradient id="lab2" x1="0" y1="0" x2="1" y2="0">
        <stop offset="0" stop-color="#d8dce3"/>
        <stop offset="0.45" stop-color="#8fa0b5"/>
        <stop offset="0.75" stop-color="#3f86c9"/>
        <stop offset="1" stop-color="#5aa3dc"/>
      </linearGradient>
    </defs>
    <polygon points="0,0 1096,0 1096,444 0,360" fill="url(#lab2)"/>
  </svg>
  <p class="heading abs" style="left:17px;top:466px;width:1040px;font-size:34px;line-height:43px">Fusce sollicitudin lorem et luctus volutpat. Proin placerat dapibus gravida. In tristique tristique nulla eget hendrerit.</p>
  <p class="abs" style="left:17px;top:573px;font-size:22px;color:var(--ink)">Maecenas vel tortor accumsan quam varius imperdiet vel eget elit</p>
  <div class="badge">3</div>
  <div class="page-code">M2</div>
</section>

<!-- Slide 4: Text with image grid -->
<section class="slide" style="top:1984px">
  <h2 class="heading abs" style="left:17px;top:55px;font-size:40px">Etiam vel massa</h2>
  <div class="rule" style="left:17px;top:113px"></div>
  <p class="abs" style="left:17px;top:148px;width:470px;font-size:20px;line-height:29px;color:var(--ink)">Quisque aliquet ex nec est vestibulum pulvinar. Pellentesque convallis molestie enim</p>
  <div class="copy abs" style="left:17px;top:222px;width:462px">
    <p>Vivamus lacus justo, ultrices nec erat in, euismod iaculis mauris. Vivamus eleifend vitae nulla vel malesuada. In ac malesuada lacus, et consectetur ante. Fusce vitae lectus sit amet mi pulvinar maximus. Aenean placerat, nibh vel accumsan aliquet, magna nibh accumsan nibh, ac tempus nunc ipsum ac tellus. Cras augue magna, placerat eget nulla non, congue suscipit neque.</p>
    <p>Proin a dolor mauris. Vestibulum ante ipsum primis in faucibus orci luctus et ultrices posuere cubilia Curae; Vestibulum eget nisl metus. Phasellus nisl est, condimentum vitae faucibus in, sollicitudin vel metus. Nunc sit amet consequat risus. Curabitur ac elit leo. In eleifend dui tellus, in scelerisque elit porttitor et. Integer eu massa lacinia, lacinia nulla non, volutpat purus. Sed libero felis, vestibulum et dolor eget, lacinia aliquet neque.</p>
  </div>
  <div class="abs" role="img" aria-label="Photo of a researcher at laboratory equipment" style="left:548px;top:63px;width:531px;height:239px;background:linear-gradient(120deg,#c9ced6,#eef0f3 60%,#d6c9b0)"></div>
  <div class="abs" role="img" aria-label="Photo of a researcher reviewing data on screens" style="left:548px;top:314px;width:257px;height:239px;background:linear-gradient(135deg,#b9c2cf,#e4e8ee)"></div>
  <div class="abs" role="img" aria-label="Photo of a gloved hand at a sample freezer" style="left:814px;top:314px;width:265px;height:239px;background:linear-gradient(135deg,#c7c9cc,#e7d6d2 55%,#eef0f2)"></div>
  <div class="badge">4</div>
  <div class="page-code">M2</div>
</section>

<!-- Slide 5: List with round image -->
<section class="slide" style="top:2627px">
  <svg class="abs" style="left:0;top:0" width="1096" height="617" aria-hidden="true">
    <circle cx="1071" cy="588" r="230" fill="var(--grey)" opacity="0.75"/>
  </svg>
  <h2 class="heading abs" style="left:17px;top:49px;font-size:40px">Praesent quis risus</h2>
  <div class="rule" style="left:17px;top:111px"></div>
  <p class="copy abs" style="left:17px;top:139px;width:460px">Proin porta fermentum ipsum, vel porttitor turpis venenatis luctus. Vivamus volutpat eu sapien quis tempus. Aenean feugiat viverra lorem ac sagittis. Donec sit amet lectus nec mi tempor laoreet ac nec nunc.</p>
  <ul class="bullets abs" style="left:17px;top:229px">
    <li><svg width="13" height="13" viewBox="0 0 13 13"><circle cx="6.5" cy="6.5" r="6.5" fill="var(--magenta)"/><path d="M5 3.8 7.8 6.5 5 9.2" stroke="#fff" stroke-width="1.8" fill="none"/></svg>Nullam accumsan purus vel tempus viverra</li>
    <li><svg width="13" height="13" viewBox="0 0 13 13"><circle cx="6.5" cy="6.5" r="6.5" fill="var(--magenta)"/><path d="M5 3.8 7.8 6.5 5 9.2" stroke="#fff" stroke-width="1.8" fill="none"/></svg>Mauris suscipit felis id nunc elementum varius</li>
    <li><svg width="13" height="13" viewBox="0 0 13 13"><circle cx="6.5" cy="6.5" r="6.5" fill="var(--magenta)"/><path d="M5 3.8 7.8 6.5 5 9.2" stroke="#fff" stroke-width="1.8" fill="none"/></svg>Praesent elementum nulla sit</li>
    <li><svg width="13" height="13" viewBox="0 0 13 13"><circle cx="6.5" cy="6.5" r="6.5" fill="var(--magenta)"/><path d="M5 3.8 7.8 6.5 5 9.2" stroke="#fff" stroke-width="1.8" fill="none"/></svg>Nam et tortor ante iaculis porttitor luctus</li>
    <li><svg width="13" height="13" viewBox="0 0 13 13"><circle cx="6.5" cy="6.5" r="6.5" fill="var(--magenta)"/><path d="M5 3.8 7.8 6.5 5 9.2" stroke="#fff" stroke-width="1.8" fill="none"/></svg>Vivamus gravida sem a pretium euismod</li>
    <li><svg width="13" height="13" viewBox="0 0 13 13"><circle cx="6.5" cy="6.5" r="6.5" fill="var(--magenta)"/><path d="M5 3.8 7.8 6.5 5 9.2" stroke="#fff" stroke-width="1.8" fill="none"/></svg>Nam lobortis purus et fringilla tempus</li>
    <li><svg width="13" height="13" viewBox="0 0 13 13"><circle cx="6.5" cy="6.5" r="6.5" fill="var(--magenta)"/><path d="M5 3.8 7.8 6.5 5 9.2" stroke="#fff" stroke-width="1.8" fill="none"/></svg>Vestibulum facilisis dolor at purus tincidunt porta</li>
    <li><svg width="13" height="13" viewBox="0 0 13 13"><circle cx="6.5" cy="6.5" r="6.5" fill="var(--magenta)"/><path d="M5 3.8 7.8 6.5 5 9.2" stroke="#fff" stroke-width="1.8" fill="none"/></svg>Nam fringilla nulla condimentum</li>
    <li><svg width="13" height="13" viewBox="0 0 13 13"><circle cx="6.5" cy="6.5" r="6.5" fill="var(--magenta)"/><path d="M5 3.8 7.8 6.5 5 9.2" stroke="#fff" stroke-width="1.8" fill="none"/></svg>Phasellus blandit quam a ipsum gravida dapibus</li>
  </ul>
  <svg class="abs" style="left:0;top:0" width="1096" height="617" role="img" aria-label="Round photo of a scientist using a microscope in a blue-lit laboratory">
    <defs>
      <radialGradient id="lab3" cx="0.45" cy="0.45" r="0.6">
        <stop offset="0" stop-color="#5d7fb0"/>
        <stop offset="1" stop-color="#132a52"/>
      </radialGradient>
    </defs>
    <circle cx="825" cy="304" r="254" fill="url(#lab3)"/>
    <circle cx="638" cy="119" r="67" fill="var(--orange)"/>
    <circle cx="738" cy="72" r="29" fill="var(--berry)"/>
  </svg>
  <div class="badge">5</div>
  <div class="page-code">M2</div>
</section>

<!-- Slide 6: Thank you -->
<section class="slide" style="top:3269px">
  <div class="abs" role="img" aria-label="Soft background image of translucent molecules" style="left:0;top:0;width:1096px;height:617px;background:radial-gradient(ellipse at 50% 50%,#ffffff 0%,#eceaf2 45%,#cfcbd8 100%)"></div>
  <div class="wordmark abs" style="left:0;width:1096px;top:195px;font-size:74px;justify-content:center">brivora<span class="dot"></span></div>
  <h2 class="abs" style="left:0;width:1096px;top:306px;text-align:center;font-size:56px;font-weight:700;color:var(--ink);line-height:1">Thank You</h2>
  <div class="rule" style="left:480px;top:389px"></div>
  <p class="abs" style="left:248px;width:600px;top:412px;text-align:center;font-size:16.5px;line-height:29px;font-weight:600;color:var(--ink)">Mauris placerat eros lorem, vel egestas mi mattis eget. Donec a nisl vel ante tristique mollis nec quis.</p>
  <div class="badge">6</div>
  <div class="page-code">M2</div>
</section>

</body>
</html>
```